Stationery Design Project

KV7 Staffing requires letterhead and business card designs for a company based in London. Just like the name, we're a management resourcing company, providing resources to third party companies. You can see www.kv7staffing.example for ideas on existing colour schemes and design concepts that have been implimented and agreed to. Ultimately the design should broadcast professionalism, safety and the concept of growth.

Target Market(s)

Financial institutes; friendly societies (All UK based)

Industry/Entity Type

Safety

Requirements
Must have
• Files produced should be print ready; and the text in them editable (eg address, name etc)

```html
<!DOCTYPE html>
<html lang="en">
<head>
<meta charset="utf-8">
<title>KV7 Staffing — Letterhead</title>
<link rel="stylesheet" href="https://fonts.googleapis.com/css2?family=Arimo:wght@400;700&family=Didact+Gothic&display=swap">
<style>
  :root {
    --page-border: #2b6ea3;
    --brand-teal: #1b8c93;
    --label-blue: #2aa2cb;
    --text-dark: #3a3a3a;
    --footer-rule: #1f8e95;
    --watermark: #bfe0ea;
    --canvas: #ffffff;
  }
  * { margin: 0; padding: 0; box-sizing: border-box; }
  html, body { width: 1200px; height: 900px; overflow: hidden; background: var(--canvas); }
  .canvas { position: relative; width: 1200px; height: 900px; }
  .letterhead {
    position: absolute; left: 282px; top: 0; width: 636px; height: 900px;
    border: 1px solid var(--page-border); background: var(--canvas);
  }
  .brand {
    position: absolute; top: 16px; left: 0; right: 0;
    display: flex; justify-content: center; align-items: center; gap: 12px;
  }
  .brand-mark { width: 30px; height: 30px; background: var(--brand-teal); }
  .brand-name {
    font-family: "Arimo", Arial, sans-serif; font-weight: 700;
    font-size: 42px; color: var(--brand-teal); letter-spacing: 0.5px; line-height: 1;
  }
  .contact-line {
    position: absolute; top: 79px; left: 30px; right: 30px;
    display: flex; justify-content: space-between; align-items: center;
    font-size: 9.5px; white-space: nowrap;
  }
  .contact-line .address { font-family: "Arimo", Arial, sans-serif; font-weight: 700; color: var(--label-blue); }
  .contact-line .label { font-family: "Arimo", Arial, sans-serif; font-weight: 700; color: var(--label-blue); }
  .contact-line .value { font-family: "Didact Gothic", Arial, sans-serif; color: var(--text-dark); }
  .contact-line .email { font-family: "Arimo", Arial, sans-serif; color: var(--text-dark); }
  .contact-line .sep { color: var(--label-blue); font-family: "Arimo", Arial, sans-serif; }
  .watermark { position: absolute; left: 135px; top: 235px; width: 365px; height: 500px; }
  .footer-rule {
    position: absolute; left: 280px; top: 872px; width: 640px; height: 2px; background: var(--footer-rule);
  }
  .footer-text {
    position: absolute; left: 282px; top: 881px; width: 636px; text-align: center;
    font-family: "Arimo", Arial, sans-serif; font-size: 9.5px; color: var(--text-dark);
    word-spacing: 1px;
  }
  .footer-text .sep { margin: 0 8px; }
</style>
</head>
<body>
<div class="canvas">
  <div class="letterhead">
    <header class="brand">
      <span class="brand-mark"></span>
      <span class="brand-name">KV7 Staffing</span>
    </header>
    <div class="contact-line">
      <span class="address">18 Harbour Row, London</span>
      <span class="sep">|</span>
      <span><span class="label">M.</span> <span class="value">1-604-318-552</span></span>
      <span class="sep">|</span>
      <span><span class="label">T.</span> <span class="value">0207 946-0318</span></span>
      <span class="sep">|</span>
      <span><span class="label">F.</span> <span class="value">0207 946-0319</span></span>
      <span class="sep">|</span>
      <span><span class="label">E.</span><span class="email">danielk@kv7staffing.example</span></span>
    </div>
    <svg class="watermark" viewBox="0 0 365 500" role="img" aria-label="Faint brand decoration area">
      <defs>
        <radialGradient id="wmFade" cx="50%" cy="55%" r="50%">
          <stop offset="0%" stop-color="#bfe0ea" stop-opacity="0.55"/>
          <stop offset="100%" stop-color="#bfe0ea" stop-opacity="0.15"/>
        </radialGradient>
      </defs>
      <circle cx="182" cy="270" r="180" fill="url(#wmFade)"/>
    </svg>
  </div>
  <div class="footer-rule"></div>
  <footer class="footer-text">www.kv7staffing.example<span class="sep">|</span>VAT No. 41726038</footer>
</div>
</body>
</html>
```